Ridgeline Talent Associates Business Card Design

We need a business card design for our new company - Ridgeline Talent Associates. RLTA is a recruitment firm that focuses on recruiting engineers and geologist for mid-size oil and gas companies. We would like our logo on the business card, which is attached, and we would like the color scheme on business cards to coordinate with our logo.

Industry/Entity Type

Oil And Gas

Contact Information for Business Card

Dana Whitlow, Founder and Managing Partner, dmw@ridgelinetalentco.org, 888.507.3942 (work), 5730915.0600 (cell), 573.642.1907 (fax), www.ridgelinetalentco.org

```html
<!DOCTYPE html>
<html lang="en">
<head>
<meta charset="utf-8">
<title>Ridgeline Talent Associates – Business Card</title>
<link href="https://fonts.googleapis.com/css2?family=Cinzel:wght@500;600&family=Lato:wght@400;700&display=swap" rel="stylesheet">
<style>
  :root {
    --backdrop: #4a4a4a;
    --navy: #23326f;
    --navy-glow: #254a8c;
    --band-top: #1f4488;
    --band-bottom: #243a7c;
    --band-edge: #1a1f3a;
    --tab-dark: #1c1c1c;
    --tab-light: #3a3a3a;
    --white: #ffffff;
    --ink-navy: #213f80;
  }
  * { box-sizing: border-box; margin: 0; padding: 0; }
  html, body { width: 1200px; height: 1000px; overflow: hidden; }
  body { background: var(--backdrop); position: relative; font-family: "Lato", sans-serif; }

  .card { position: absolute; width: 612px; height: 360px; box-shadow: 0 3px 0 #1b1b1b, 0 6px 14px rgba(0,0,0,.35); overflow: hidden; }

  .card-front { left: 145px; top: 125px;
    background: radial-gradient(ellipse 55% 60% at 50% 38%, var(--navy-glow), var(--navy) 75%); }

  .brand { position: absolute; left: 0; right: 0; display: flex; flex-direction: column; align-items: center; }
  .brand-mark { width: 58px; height: 58px; border-radius: 50%; }
  .brand-name { font-family: "Cinzel", serif; font-weight: 600; font-size: 25px; letter-spacing: .5px; margin-top: 16px; white-space: nowrap; }

  .card-front .brand { top: 122px; }
  .card-front .brand-mark { background: var(--white); }
  .card-front .brand-name { color: var(--white); }

  .card-back { left: 415px; top: 534px; background: var(--white); }
  .card-back .brand { top: 48px; }
  .card-back .brand-mark { background: var(--ink-navy); }
  .card-back .brand-name { color: var(--ink-navy); }

  .contact-band { position: absolute; left: 0; right: 0; top: 210px; height: 150px;
    background: linear-gradient(180deg, var(--band-top), var(--band-bottom));
    border-bottom: 4px solid var(--band-edge); }

  .name-tab { position: absolute; right: 0; top: 0; width: 287px; height: 51px;
    background: linear-gradient(180deg, var(--tab-light), var(--tab-dark));
    clip-path: polygon(0 0, 100% 0, 100% 100%, 16px 100%);
    color: var(--white); padding: 5px 0 0 52px; }
  .person-name { font-family: "Cinzel", serif; font-weight: 500; font-size: 19px; letter-spacing: 1px; line-height: 22px; }
  .person-role { font-size: 13.5px; line-height: 18px; }

  .contact-list { position: absolute; left: 37px; top: 13px; list-style: none; }
  .contact-list li { display: flex; align-items: center; height: 23.5px; color: var(--white); font-size: 14px; }
  .contact-list svg { width: 16px; height: 16px; margin-right: 12px; fill: var(--white); }
</style>
</head>
<body>

<section class="card card-front" aria-label="Card front">
  <div class="brand">
    <span class="brand-mark"></span>
    <span class="brand-name">Ridgeline Talent Associates</span>
  </div>
</section>

<section class="card card-back" aria-label="Card back">
  <div class="brand">
    <span class="brand-mark"></span>
    <span class="brand-name">Ridgeline Talent Associates</span>
  </div>

  <div class="contact-band">
    <ul class="contact-list">
      <li><svg viewBox="0 0 16 16"><path d="M3 1l3 3-1.5 2a9 9 0 0 0 5.5 5.5L12 10l3 3-2 2C7 15 1 9 1 3z"/></svg>888.507.3942</li>
      <li><svg viewBox="0 0 16 16"><path d="M4 0h8v16H4zM5.5 2v10h5V2zM7 13.5h2v1H7z" fill-rule="evenodd"/></svg>5730915.0600</li>
      <li><svg viewBox="0 0 16 16"><path d="M4 1h8v4H4zM1 6h14v6h-3v3H4v-3H1zM5 10v4h6v-4z" fill-rule="evenodd"/></svg>573.642.1907</li>
      <li><svg viewBox="0 0 16 16"><path d="M1 3h14v1.5L8 9 1 4.5zM1 6.3l7 4.5 7-4.5V13H1z"/></svg>dmw@ridgelinetalentco.org</li>
      <li><svg viewBox="0 0 16 16"><circle cx="8" cy="8" r="7"/><path d="M4 5l3 1 0 3-2 2zM9 3l3 2-1 3 2 2-3 2z" fill="#1f4488"/></svg>www.ridgelinetalentco.org</li>
    </ul>

    <div class="name-tab">
      <div class="person-name">DANA WHITLOW</div>
      <div class="person-role">Founder &amp; Managing Partner</div>
    </div>
  </div>
</section>

</body>
</html>
```